Automotive Accessories Business Card

Design a business template that match our new logo design and our industry.

https://www.kelvorauto.com/

Target Market(s)

Aftermarket auto parts and accessories

Industry/Entity Type

automotive

Contact Information for Business Card

company logo

Font styles to use
Serif
Sans Serif

Colors
EB3D1F
EC4F4E
F09395
F8D3D4
FCEDEE

```html
<!DOCTYPE html>
<html lang="en">
<head>
<meta charset="utf-8">
<title>Kelvor Auto – Business Card</title>
<link href="https://fonts.googleapis.com/css2?family=Exo+2:wght@400;600;700&display=swap" rel="stylesheet">
<style>
  :root {
    --stage: #8f8f8f;
    --brand-red: #d71f26;
    --paper: #ffffff;
    --charcoal: #3f3f3f;
    --ink: #1c1c1c;
    --text-light: #ffffff;
  }
  html, body {
    margin: 0;
    padding: 0;
    width: 1200px;
    height: 1200px;
    overflow: hidden;
    background: var(--stage);
    font-family: "Exo 2", sans-serif;
  }
  .canvas {
    position: relative;
    width: 1200px;
    height: 1200px;
  }
  .card {
    position: absolute;
    left: 281px;
    width: 638px;
    height: 365px;
    border-radius: 24px;
    overflow: hidden;
    box-shadow: 0 4px 8px rgba(0,0,0,0.35);
  }
  .card--front { top: 195px; background: var(--paper); }
  .card--back  { top: 640px; background: var(--brand-red); }

  .front-art {
    position: absolute;
    inset: 0;
    width: 638px;
    height: 365px;
  }
  .front-art .red-field { fill: var(--brand-red); }
  .front-art .swoosh { fill: var(--charcoal); }

  .contact {
    position: absolute;
    left: 42px;
    top: 80px;
    color: var(--text-light);
  }
  .contact__name {
    margin: 0;
    font-size: 29px;
    font-weight: 700;
    letter-spacing: 1px;
    line-height: 1;
  }
  .contact__title {
    margin: 4px 0 0;
    font-size: 16px;
    font-weight: 400;
  }
  .contact__list {
    list-style: none;
    margin: 14px 0 0;
    padding: 0;
    font-size: 15.5px;
    line-height: 21.5px;
  }
  .contact__item {
    position: relative;
    padding-left: 28px;
  }
  .contact__item--address { margin-bottom: 8px; }
  .contact__icon {
    position: absolute;
    left: 0;
    top: 4px;
    width: 14px;
    height: 14px;
    fill: var(--text-light);
  }

  .wordmark {
    position: absolute;
    display: flex;
    align-items: center;
    font-weight: 700;
    white-space: nowrap;
  }
  .wordmark__square { display: block; flex: none; }
  .wordmark--front {
    left: 378px;
    top: 162px;
    gap: 8px;
    font-size: 27px;
    letter-spacing: 0.5px;
    color: var(--charcoal);
  }
  .wordmark--front .wordmark__square {
    width: 18px; height: 18px; background: var(--brand-red);
  }
  .wordmark--back {
    left: 0;
    right: 0;
    top: 145px;
    gap: 10px;
    justify-content: center;
    font-size: 70px;
    letter-spacing: 1px;
    color: var(--ink);
  }
  .wordmark--back .wordmark__square {
    width: 44px; height: 44px; background: var(--ink);
  }
</style>
</head>
<body>
<main class="canvas">

  <section class="card card--front" aria-label="Business card front">
    <svg class="front-art" viewBox="0 0 638 365" aria-hidden="true">
      <path class="red-field" d="M0,0 H150 C230,5 272,70 305,150 C345,245 380,345 525,365 H0 Z"/>
      <path class="swoosh" d="M200,12 C262,32 294,100 326,170 C360,250 385,330 505,363 C398,345 366,268 334,188 C306,116 280,44 200,12 Z"/>
    </svg>

    <div class="contact">
      <h1 class="contact__name">DANIEL REYES</h1>
      <p class="contact__title">Founder &amp; CEO</p>
      <ul class="contact__list">
        <li class="contact__item contact__item--address">
          <svg class="contact__icon" viewBox="0 0 14 14"><path d="M7 0a5 5 0 0 0-5 5c0 3.6 5 9 5 9s5-5.4 5-9a5 5 0 0 0-5-5zm0 7a2 2 0 1 1 0-4 2 2 0 0 1 0 4z"/></svg>
          240 W. Harbor Ave. Unit B<br>Fairview, CA, 90210<br>United States
        </li>
        <li class="contact__item">
          <svg class="contact__icon" viewBox="0 0 14 14"><path d="M3 0l2.4 3-1.2 1.8c.8 1.8 2.2 3.2 4 4L10 7.6 13 10l-1.2 2.8C6 13 1 8 1.2 2.2z"/></svg>
          1-800-555-0142
        </li>
        <li class="contact__item">
          <svg class="contact__icon" viewBox="0 0 14 14"><path d="M0 3h14v1L7 8 0 4zm0 2.5l7 4 7-4V12H0z"/></svg>
          sales@kelvorauto.com
        </li>
        <li class="contact__item">
          <svg class="contact__icon" viewBox="0 0 14 14"><circle cx="7" cy="7" r="6.5"/><path d="M4 4c1 0 2 1 1.5 2S3 7 4 9l1 2M9 2c-1 1 0 2 1 2s2 1 1 3" stroke="#d71f26" stroke-width="1.2" fill="none"/></svg>
          kelvorauto.com
        </li>
      </ul>
    </div>

    <div class="wordmark wordmark--front">
      <span class="wordmark__square"></span>
      <span class="wordmark__name">KELVOR AUTO</span>
    </div>
  </section>

  <section class="card card--back" aria-label="Business card back">
    <div class="wordmark wordmark--back">
      <span class="wordmark__square"></span>
      <span class="wordmark__name">KELVOR AUTO</span>
    </div>
  </section>

</main>
</body>
</html>
```